Ferncrest Dental, LLC business card project

Business card to be designed with current logo.
Dental office- please keep design of card that looks clean and professional.
Please include the following info:
Ferncrest Dental, LLC
Dr. Lorna Pettigrew
2871 Marlowe Street
Bethlehem, PA 18093
610-555-0193
ferncrestdental.office@examplemail.test
Hello everyone-
Reason: Just got back from overseas- will look at all designs and provide feedback. Thank you!
Reason: Polling my friends for the final selection-
thank you to all those that participated- so many talented designers!

```html
<!DOCTYPE html>
<html lang="en">
<head>
<meta charset="utf-8">
<title>Ferncrest Dental, LLC – Business Card</title>
<link rel="stylesheet" href="https://fonts.googleapis.com/css2?family=Arimo:wght@400;700&display=swap">
<style>
  :root {
    --page: #ffffff;
    --green-light: #86d800;
    --green-mid: #62c000;
    --green-deep: #45a500;
    --brand-green: #6cc51a;
    --band: #ffffff;
    --ink-on-green: #ffffff;
  }
  * { margin: 0; padding: 0; box-sizing: border-box; }
  html, body {
    width: 1000px; height: 1200px; overflow: hidden;
    background: var(--page);
    font-family: "Arimo", Arial, Helvetica, sans-serif;
  }
  .card {
    position: absolute;
    left: 62px; width: 848px; height: 522px;
    overflow: hidden;
    box-shadow: 0 3px 10px rgba(0,0,0,0.18);
  }
  .card--front { top: 47px; }
  .card--back { top: 630px; }
  .card__texture {
    position: absolute; inset: 0;
    background: radial-gradient(ellipse at 50% 50%, var(--green-light) 0%, var(--green-mid) 55%, var(--green-deep) 100%);
  }
  .brand-band {
    position: absolute; left: 0; right: 0;
    background: var(--band);
    display: flex; align-items: center; justify-content: center; gap: 18px;
  }
  .card--front .brand-band { top: 193px; height: 138px; }
  .card--back .brand-band {
    top: 37px; height: 105px;
    box-shadow: 0 4px 8px rgba(0,0,0,0.25);
  }
  .brand-band__dot {
    width: 30px; height: 30px; border-radius: 50%;
    background: var(--brand-green);
  }
  .brand-band__name {
    font-size: 56px; font-weight: 400; color: var(--brand-green);
    letter-spacing: -0.5px; line-height: 1;
  }
  .contact {
    position: absolute; left: 33px; top: 178px;
    color: var(--ink-on-green);
  }
  .contact__name {
    font-size: 58px; font-weight: 700; line-height: 1; letter-spacing: -0.5px;
  }
  .contact__address {
    margin-top: 10px;
    font-size: 34px; font-weight: 400; line-height: 47px;
  }
  .contact__lines { margin-top: 42px; margin-left: 14px; }
  .contact__line {
    display: flex; align-items: center; gap: 20px;
    font-size: 33px; font-weight: 700; height: 52px;
  }
  .contact__icon { width: 44px; height: 44px; flex: none; }
</style>
</head>
<body>
  <section class="card card--front">
    <div class="card__texture" role="img" aria-label="Green geometric repeating pattern background"></div>
    <div class="brand-band">
      <span class="brand-band__dot"></span>
      <span class="brand-band__name">Ferncrest Dental</span>
    </div>
  </section>

  <section class="card card--back">
    <div class="card__texture" role="img" aria-label="Green geometric repeating pattern background"></div>
    <div class="brand-band">
      <span class="brand-band__dot"></span>
      <span class="brand-band__name">Ferncrest Dental</span>
    </div>
    <div class="contact">
      <h1 class="contact__name">Dr. Lorna Pettigrew</h1>
      <p class="contact__address">2871 Marlowe Street<br>Bethlehem, PA 18093</p>
      <div class="contact__lines">
        <p class="contact__line">
          <svg class="contact__icon" viewBox="0 0 44 44" aria-hidden="true">
            <circle cx="22" cy="22" r="19" fill="none" stroke="#fff" stroke-width="3"/>
            <path d="M15 12c2-1 3 0 4 2l1 3c0 1-1 2-2 3 1 3 4 6 7 7 1-1 2-2 3-2l3 1c2 1 3 2 2 4-1 2-3 3-5 3-8-1-15-8-16-16 0-2 1-4 3-5z" fill="#fff"/>
          </svg>
          <span>610-555-0193</span>
        </p>
        <p class="contact__line">
          <svg class="contact__icon" viewBox="0 0 44 44" aria-hidden="true">
            <rect x="4" y="10" width="36" height="24" fill="none" stroke="#fff" stroke-width="3"/>
            <path d="M4 10l18 14 18-14M4 34l13-12M40 34l-13-12" fill="none" stroke="#fff" stroke-width="3"/>
          </svg>
          <span>ferncrestdental.office@examplemail.test</span>
        </p>
      </div>
    </div>
  </section>
</body>
</html>
```